Brackenfield Partners Exit Plan business consultant web site

This website is for a consulting business that helps other businesses with exit plans. Essentially, assists them with the sale of their business. This website should be very professional, almost with a wall street look. I would like a very attractive image on the homepage. Perhaps something that denotes success. Perhaps a picture of palm trees and a beach? I will leave it to you for interpretation.

Across the screen I would like the words "Does your business have an exit plan?"

Below that it should read the following:
Let us help you with a completely impartial, no obligation assessment (button with link to the contact page)

Also, please use logo in a prominent place on the website so it's easily seen.

Target Market(s)

Males 40+

Coding

Coded - Design and coding required

Number of Pages Required

5+ page

Colors

Designer to choose colors to be used in the design.

Requirements
Must have
• The tabs for the homepage on the top should be:
• 1. About us
• 2. Services
• 3. Industries
• 4. Our success
• 5. Contact
Nice to have
• Clean, professional image.
• Please put FB, Twitter, Linked In - logos at bottom.
• Here are two examples of a website to give you an idea:
• https://journal.corvanteriq.com/library/why-every-business-owner-should-have-an-exit-plan
Should not have
• nothing whimsical or cartoon like

```html
<!DOCTYPE html>
<html lang="en">
<head>
<meta charset="utf-8">
<title>Brackenfield Partners — Exit Planning</title>
<link href="https://fonts.googleapis.com/css2?family=Cinzel:wght@400;600;700&family=Open+Sans:wght@400;600;700&display=swap" rel="stylesheet">
<style>
  :root{
    --ink:#1c2230;
    --navy:#1f2a3d;
    --charcoal:#17181b;
    --slate:#3a4558;
    --steel:#6f7f96;
    --mist:#dfe6ee;
    --paper:#ffffff;
    --soft:#f4f5f7;
    --line:#d6d9de;
    --muted:#6b707a;
    --gold:#b89a5e;
  }
  *{box-sizing:border-box;margin:0;padding:0}
  html,body{width:1200px;height:2800px;overflow:hidden;background:var(--paper)}
  body{font-family:"Open Sans",Arial,sans-serif;color:var(--ink)}
  .page{width:1200px;height:2800px;display:flex;flex-direction:column}

  .site-nav{height:40px;flex:none;background:var(--charcoal);display:flex;align-items:center;justify-content:space-between;padding:0 70px}
  .brand{display:flex;align-items:center;gap:10px;color:var(--paper);font-family:"Cinzel",serif;font-weight:600;font-size:13px;letter-spacing:2px;text-transform:uppercase}
  .brand-mark{width:16px;height:16px;background:var(--paper)}
  .nav-links{display:flex;gap:26px;list-style:none}
  .nav-links li{color:var(--paper);font-size:10px;font-weight:600;letter-spacing:1.5px}

  .hero{height:620px;flex:none;position:relative;display:flex;align-items:center;justify-content:center;
    background:linear-gradient(180deg,#26334a 0%,#4d617d 22%,#b9c7d6 45%,#e9eef3 55%,#8fa1b6 72%,#2c3a52 100%)}
  .hero-title{position:relative;text-align:center;font-family:"Cinzel",serif;color:var(--navy);line-height:1.1}
  .hero-title .line1{display:block;font-size:56px;font-weight:400;letter-spacing:6px}
  .hero-title .line2{display:block;font-size:62px;font-weight:700;letter-spacing:5px}

  .intro{height:330px;flex:none;text-align:center;padding-top:58px}
  .intro h2{font-family:"Cinzel",serif;font-size:28px;font-weight:700;letter-spacing:2px;color:var(--ink)}
  .intro .sub{font-family:"Cinzel",serif;font-size:24px;letter-spacing:2px;color:var(--ink);margin-top:4px}
  .intro p{font-size:11px;color:var(--muted);margin-top:18px}
  .partner-strip{display:flex;justify-content:center;gap:22px;margin-top:34px}
  .partner-badge{width:140px;height:56px;border-radius:4px;background:var(--soft);display:flex;align-items:center;justify-content:center}
  .partner-badge span{display:block;width:84px;height:14px;border-radius:7px;background:#c9ccd2}
  .partner-badge.featured{background:var(--paper);box-shadow:0 4px 14px rgba(0,0,0,.18)}
  .partner-badge.featured span{background:var(--navy)}

  .assessment-band{height:250px;flex:none;margin-top:20px;display:flex;flex-direction:column;align-items:center;justify-content:center;text-align:center;
    background:linear-gradient(90deg,#2a3447 0%,#4a5a74 45%,#6c7d95 60%,#34405a 100%)}
  .assessment-band h3{font-family:"Cinzel",serif;color:var(--paper);font-size:26px;font-weight:600;letter-spacing:3px;line-height:1.35}
  .btn{display:inline-block;margin-top:24px;padding:10px 30px;border:1px solid rgba(255,255,255,.7);color:var(--paper);font-size:10px;letter-spacing:2px;font-weight:600;background:rgba(255,255,255,.12)}

  .difficult{height:400px;flex:none;display:flex;gap:60px;padding:60px 150px 0}
  .difficult-copy{flex:1}
  .difficult-copy h3{font-family:"Cinzel",serif;font-size:26px;font-weight:400;letter-spacing:1.5px;color:var(--ink);line-height:1.15}
  .difficult-copy h3 strong{font-weight:700;display:block}
  .difficult-copy p{font-size:11px;line-height:1.6;color:var(--muted);margin-top:12px}
  .desk-photo{width:340px;height:240px;margin-top:10px;border:6px solid var(--paper);outline:1px solid var(--line);box-shadow:0 6px 16px rgba(0,0,0,.15);
    background:linear-gradient(160deg,#e9ecef 0%,#c4ccd5 45%,#5a6474 75%,#2c3340 100%)}

  .first-step{height:380px;flex:none;text-align:center;padding-top:40px;border-top:1px solid var(--soft)}
  .first-step .kicker{font-family:"Cinzel",serif;font-size:24px;letter-spacing:2px;color:var(--ink)}
  .first-step h3{font-family:"Cinzel",serif;font-size:24px;font-weight:700;letter-spacing:2px;color:var(--ink)}
  .first-step p{width:720px;margin:14px auto 0;font-size:11px;line-height:1.6;color:var(--muted)}
  .team-cards{display:flex;justify-content:center;gap:20px;margin-top:40px}
  .team-card{width:150px;height:74px;background:var(--paper);box-shadow:0 4px 14px rgba(0,0,0,.14);display:flex;align-items:center;justify-content:center;padding:0 12px;font-size:11px;line-height:1.35;color:var(--ink)}

  .institute-band{height:360px;flex:none;display:flex;flex-direction:column;align-items:center;justify-content:center;text-align:center;position:relative;
    background:linear-gradient(90deg,#1f2632 0%,#3d4657 40%,#58627a 55%,#2a3140 100%)}
  .institute-band h3{font-family:"Cinzel",serif;color:var(--paper);font-size:26px;font-weight:600;letter-spacing:3px}
  .institute-band p{width:620px;margin-top:14px;font-size:11px;line-height:1.6;color:#d8dde5}
  .scroll-dot{position:absolute;bottom:-16px;left:584px;width:32px;height:32px;border-radius:50%;background:var(--charcoal);display:flex;align-items:center;justify-content:center}

  .site-footer{height:350px;flex:none;display:flex;flex-direction:column;align-items:center;justify-content:center;gap:16px}
  .footer-mark{width:60px;height:60px;background:var(--charcoal)}
  .footer-name{font-family:"Cinzel",serif;font-size:20px;font-weight:600;letter-spacing:3px;color:var(--charcoal);text-transform:uppercase}
  .social{display:flex;gap:10px}
  .social span{width:22px;height:22px;background:var(--charcoal)}

  .legal-bar{height:50px;flex:none;background:var(--charcoal);display:flex;align-items:center;justify-content:center;gap:34px;color:#aeb3bb;font-size:10px;letter-spacing:.5px}
</style>
</head>
<body>
<div class="page">
  <header class="site-nav">
    <div class="brand"><span class="brand-mark"></span>Brackenfield Partners</div>
    <ul class="nav-links">
      <li>ABOUT US</li><li>SERVICES</li><li>INDUSTRIES</li><li>OUR SUCCESS</li><li>CONTACT</li>
    </ul>
  </header>

  <section class="hero" role="img" aria-label="Businessman in a suit seen from behind, looking out over a bright city skyline">
    <h1 class="hero-title"><span class="line1">DOES YOUR BUSINESS</span><span class="line2">HAVE AN EXIT PLAN?</span></h1>
  </section>

  <section class="intro">
    <h2>BRACKENFIELD PARTNERS IS A MODERN COMPANY</h2>
    <div class="sub">OFFERING BUSINESS PLANNING AND EXPERT SERVICES.</div>
    <p>We help business owners and investors map the transition of ownership and prepare every step of the sale with care.</p>
    <div class="partner-strip">
      <div class="partner-badge"><span></span></div>
      <div class="partner-badge"><span></span></div>
      <div class="partner-badge featured"><span></span></div>
      <div class="partner-badge"><span></span></div>
      <div class="partner-badge"><span></span></div>
    </div>
  </section>

  <section class="assessment-band" role="img" aria-label="Business people shaking hands in an office">
    <h3>LET US HELP YOU WITH A COMPLETELY<br>IMPARTIAL, NO OBLIGATION ASSESSMENT</h3>
    <span class="btn">GET STARTED</span>
  </section>

  <section class="difficult">
    <div class="difficult-copy">
      <h3>A DIFFICULT TOPIC FOR MANY<strong>BUSINESS OWNERS</strong></h3>
      <p>Because many business owners have been involved with their company for years, they see it as the foundation of a life of hard work and sacrifice. That can make it difficult to consider letting go. As a result, most owners put off the subject of an exit plan until change is forced upon them.</p>
      <p>It's not that business owners aren't aware of the value of planning. According to research from the Harrowgate Exit Institute, most owners believe an exit plan is important, yet fewer than one in four have a written plan in place. Many have never spoken with an advisor about their options.</p>
      <p>On average, 80% of a business owner's net worth is tied up in the business, so the risk of not having a solid exit plan is simply too great to ignore.</p>
    </div>
    <div class="desk-photo" role="img" aria-label="Business owner in a suit seated at a desk with a laptop in a bright office"></div>
  </section>

  <section class="first-step">
    <div class="kicker">THE FIRST STEP:</div>
    <h3>ASSEMBLING AN EXIT-PLANNING TEAM</h3>
    <p>As with most plans, the best starting point is surrounding yourself with the right team of advisors and making sure everyone is on the same page. The composition of teams may differ depending on the type of business, but consider starting with the following experts:</p>
    <div class="team-cards">
      <div class="team-card">Accountant</div>
      <div class="team-card">Investment banker/M&amp;A advisor</div>
      <div class="team-card">Corporate attorney</div>
      <div class="team-card">Trust and estate attorney</div>
      <div class="team-card">Wealth planning investment advisor</div>
    </div>
  </section>

  <section class="institute-band" role="img" aria-label="Advisors meeting around a boardroom table">
    <h3>HARROWGATE EXIT INSTITUTE</h3>
    <p>Business owners who are successful with their exit plan begin early. Our team works closely with you to prepare the company, the owner and the family for the transition ahead.</p>
    <span class="btn">READ MORE</span>
    <span class="scroll-dot">
      <svg width="12" height="12" viewBox="0 0 12 12"><path d="M2 4 L6 8 L10 4" fill="none" stroke="#ffffff" stroke-width="1.6"/></svg>
    </span>
  </section>

  <footer class="site-footer">
    <div class="footer-mark"></div>
    <div class="footer-name">Brackenfield Partners</div>
    <div class="social" aria-label="Social links"><span></span><span></span><span></span></div>
  </footer>

  <div class="legal-bar">
    <span>© 2024 Brackenfield Partners</span><span>Terms of Use</span><span>Privacy Policy</span><span>Cookie Settings</span><span>Accessibility</span><span>Site Map</span>
  </div>
</div>
</body>
</html>
```